Lumen Cove Skincare - Package Design

New Beauty label needing product packaging design. Looking for elegant and stylish design to represent our premium brand.

This project is for 1 label and 1 box design. The winning designer will be assigned another project for the next product in the range. (to be paid as a new project)

This product is for "Dead Sea Mud Mask". Please see the label format and jar attached. Please note there are 2 different jars we are considering (will have a mud inside). Please feel free to choose whichever one suits your design best.

The labels and boxes are to retain the product information, such as size, ingredients etc, but is to be updated to our brand. You can move or display the other information as you wish.

the size of the dead sea mud mask color box is 72*72*85mm (length*width*height)
the size of dead sea mud mask label is 218*58mm (width*height)

Target Market(s)

Women 15 to 65

Requirements
Must have
• Must be elegant and represent our brand which is a premium beauty product.
Should not have
• Dark blue. Dark purple etc. Colours should compliment the logo

```html
<!DOCTYPE html>
<html lang="en">
<head>
<meta charset="UTF-8">
<title>Lumen Cove Skincare – Mud Mask Label and Box</title>
<link href="https://fonts.googleapis.com/css2?family=Montserrat:wght@400;600&display=swap" rel="stylesheet">
<style>
  :root {
    --backdrop: #c8c7c7;
    --label-black: #141414;
    --box-black: #121212;
    --mocha: #6e5a47;
    --mocha-deep: #4a3b2f;
    --gold: #dba823;
    --white: #ffffff;
  }
  html, body {
    margin: 0;
    padding: 0;
    width: 1200px;
    height: 1200px;
    overflow: hidden;
    background: var(--backdrop);
    font-family: "Montserrat", sans-serif;
  }
  .canvas {
    position: relative;
    width: 1200px;
    height: 1200px;
  }
  .jar-label {
    position: absolute;
    left: 80px;
    top: 90px;
    width: 1040px;
    height: 277px;
    box-shadow: 0 10px 30px rgba(0,0,0,0.25);
  }
  .box-net {
    position: absolute;
    left: 80px;
    top: 470px;
    display: flex;
    gap: 40px;
    align-items: flex-end;
  }
  .box-panel {
    position: relative;
    width: 320px;
    height: 378px;
    box-shadow: 0 10px 30px rgba(0,0,0,0.25);
    overflow: hidden;
  }
  .box-panel--top {
    height: 320px;
    background: var(--mocha-deep);
  }
  .box-panel svg,
  .jar-label svg {
    position: absolute;
    inset: 0;
    display: block;
  }
  .brand {
    position: absolute;
    display: flex;
    align-items: center;
    gap: 12px;
    color: var(--gold);
    font-weight: 600;
    white-space: nowrap;
  }
  .brand__dot {
    border: 2px solid var(--gold);
    border-radius: 50%;
    flex: none;
  }
  .jar-label .brand {
    left: 50%;
    top: 82px;
    transform: translateX(-50%);
    font-size: 30px;
    letter-spacing: 1px;
  }
  .jar-label .brand__dot { width: 26px; height: 26px; }
  .jar-label__tagline {
    position: absolute;
    left: 0;
    right: 0;
    top: 212px;
    margin: 0;
    text-align: center;
    color: var(--white);
    font-size: 13px;
    line-height: 1.3;
  }
  .jar-label__tagline strong { font-weight: 600; display: block; }
  .box-panel--front .brand {
    left: 50%;
    top: 128px;
    transform: translateX(-50%);
    font-size: 20px;
    letter-spacing: 0.5px;
  }
  .box-panel--front .brand__dot { width: 20px; height: 20px; }
  .info-copy {
    position: absolute;
    left: 26px;
    top: 30px;
    width: 268px;
    color: var(--white);
    font-size: 8.5px;
    line-height: 1.55;
  }
  .info-copy h3 {
    margin: 0 0 4px;
    color: var(--gold);
    font-size: 10px;
    font-weight: 600;
  }
  .info-copy p { margin: 0 0 18px; }
</style>
</head>
<body>
<main class="canvas">

  <section class="jar-label" aria-label="Jar label">
    <svg width="1040" height="277" viewBox="0 0 1040 277">
      <rect width="1040" height="277" fill="var(--label-black)"/>
      <path d="M0 150 C 300 150, 380 205, 520 205 C 660 205, 740 150, 1040 150 L1040 277 L0 277 Z" fill="var(--mocha)"/>
      <path d="M0 150 C 300 150, 380 205, 520 205 C 660 205, 740 150, 1040 150" fill="none" stroke="var(--gold)" stroke-width="4"/>
    </svg>
    <div class="brand"><span class="brand__dot"></span>Lumen Cove Skincare</div>
    <p class="jar-label__tagline"><strong>Lorem Ipsum</strong>has been the industry's<br>standard dummy</p>
  </section>

  <section class="box-net" aria-label="Box panels">
    <div class="box-panel box-panel--top" aria-label="Box lid"></div>

    <div class="box-panel box-panel--side" aria-label="Box side panel">
      <svg width="320" height="378" viewBox="0 0 320 378">
        <rect width="320" height="378" fill="var(--box-black)"/>
        <path d="M0 220 C 70 280, 140 340, 210 378 L0 378 Z" fill="var(--mocha)"/>
        <path d="M0 220 C 70 280, 140 340, 210 378" fill="none" stroke="var(--gold)" stroke-width="4"/>
      </svg>
      <div class="info-copy">
        <h3>Lorem Ipsum</h3>
        <p>is simply dummy text of the printing and typesetting industry. Lorem Ipsum has been the industry's standard dummy text ever since the 1500s, when an unknown printer took a galley of type and scrambled it to make a type specimen book. It has survived not only five centuries, but also the leap into electronic typesetting, remaining essentially unchanged. It was popularised</p>
        <h3>Lorem Ipsum</h3>
        <p>is simply dummy text of the printing and typesetting industry. Lorem Ipsum has been the industry's standard dummy text ever since the 1500s.</p>
      </div>
    </div>

    <div class="box-panel box-panel--front" aria-label="Box front panel">
      <svg width="320" height="378" viewBox="0 0 320 378">
        <rect width="320" height="378" fill="var(--box-black)"/>
        <path d="M0 370 C 110 322, 220 267, 320 237 L320 378 L0 378 Z" fill="var(--mocha)"/>
        <path d="M0 370 C 110 322, 220 267, 320 237" fill="none" stroke="var(--gold)" stroke-width="8"/>
      </svg>
      <div class="brand"><span class="brand__dot"></span>Lumen Cove Skincare</div>
    </div>
  </section>

</main>
</body>
</html>
```